Carton Box Packaging For Motorcycle Brake Shoe - Varonel Brand

Packaging Dimensions: 125mm (H) x 125mm (W) x 31mm (D)
We would like to design a genuine Carton box Packaging for motorcycle Brake Shoe.
This is a critical part of the motorcycle, so we need the packaging to reflect elegant impression.
Varonel, is one of the leading companies for manufacturing Motorcycles, located in Egypt. Our company is offering high-quality products, the best in the local market, with very competitive prices.
We have a limited time to get this project done, So we Highly appreciate receiving your designs ASAP.
Target Market(s)
Economical Motorcycle Buyers
Colors
Designer to choose colors to be used in the design.
Look and feel

```html
<!DOCTYPE html>
<html lang="en">
<head>
<meta charset="utf-8">
<title>Varonel Brake Shoe Kit – Carton Dieline</title>
<link rel="stylesheet" href="https://fonts.googleapis.com/css2?family=Archivo+Black&family=Montserrat:wght@600;700;800&display=swap">
<style>
  :root {
    --brand-red: #d1222b;
    --brand-blue: #1a7fd0;
    --ink: #1e1e1e;
    --panel-light: #f3f3f3;
    --panel-shade: #dcdcdc;
    --steel: #9a9a9a;
    --white: #ffffff;
  }
  html, body {
    margin: 0;
    width: 1200px;
    height: 1200px;
    overflow: hidden;
    background: var(--white);
  }
  .dieline {
    position: absolute;
    left: 20px;
    top: 194px;
    width: 1160px;
    height: 812px;
  }
  .red { fill: var(--brand-red); }
  .panel-face { fill: url(#panelGradient); }
  .headline { font-family: "Archivo Black", sans-serif; fill: var(--ink); letter-spacing: 1px; }
  .headline-light { font-family: "Archivo Black", sans-serif; fill: var(--white); letter-spacing: 1px; }
  .tagline { font-family: "Montserrat", sans-serif; font-weight: 800; fill: var(--brand-blue); }
  .side-title { font-family: "Archivo Black", sans-serif; fill: var(--white); letter-spacing: 1px; }
  .side-sub { font-family: "Montserrat", sans-serif; font-weight: 700; fill: #f1e6e6; }
  .strip-copy { font-family: "Montserrat", sans-serif; font-weight: 600; fill: var(--white); font-size: 10.5px; }
  .badge-text { font-family: "Montserrat", sans-serif; font-weight: 700; fill: var(--white); font-size: 9.5px; letter-spacing: 0.5px; }
  .brand-name { font-family: "Archivo Black", sans-serif; fill: #3a3a3a; font-size: 17px; letter-spacing: 1px; }
  .product-photo { fill: url(#steelGradient); }
  .product-thumb { fill: url(#steelGradient); }
</style>
</head>
<body>
<svg class="dieline" viewBox="0 0 1000 700" xmlns="http://www.w3.org/2000/svg">
  <defs>
    <linearGradient id="panelGradient" x1="0" y1="0" x2="1" y2="1">
      <stop offset="0" stop-color="#fafafa"/>
      <stop offset="1" stop-color="#e2e2e2"/>
    </linearGradient>
    <radialGradient id="steelGradient" cx="0.5" cy="0.5" r="0.6">
      <stop offset="0" stop-color="#ececec"/>
      <stop offset="0.6" stop-color="#b8b8b8"/>
      <stop offset="1" stop-color="#5a5a5a"/>
    </radialGradient>
    <clipPath id="stripFront1"><rect x="98" y="159" width="79" height="370"/></clipPath>
    <clipPath id="stripFront2"><rect x="560" y="159" width="78" height="370"/></clipPath>
    <clipPath id="stripTopFlap"><rect x="560" y="73" width="78" height="86"/></clipPath>
    <clipPath id="stripBottomFlap"><rect x="98" y="529" width="79" height="86"/></clipPath>
  </defs>

  <!-- Side panel A with dust flaps -->
  <g class="side-panel">
    <polygon class="red" points="6,159 18,83 68,83 95,159"/>
    <rect class="red" x="6" y="159" width="92" height="370"/>
    <polygon class="red" points="8,529 98,529 86,605 22,605"/>
    <g transform="translate(48,500) rotate(-90)">
      <text class="side-title" x="0" y="0" font-size="31">BRAKE SHOE KIT</text>
      <text class="side-sub" x="22" y="26" font-size="20">Genuineparts</text>
    </g>
  </g>

  <!-- Front panel -->
  <g class="front-panel">
    <rect class="panel-face" x="98" y="159" width="370" height="370"/>
    <rect class="red" x="98" y="159" width="79" height="370"/>
    <circle cx="285" cy="159" r="32" fill="var(--white)"/>
    <text class="strip-copy" transform="translate(121,510) rotate(-90)">Aluminum Alloy Motorcycle Brake Shoe With Spring</text>
    <rect class="product-photo" x="262" y="238" width="206" height="290" rx="90" role="img" aria-label="Photo of a motorcycle drum brake shoe pair with springs"/>
    <text class="headline" x="155" y="222" font-size="29">BRAKE SHOE KIT</text>
    <text class="headline-light" x="155" y="222" font-size="29" clip-path="url(#stripFront1)">BRAKE SHOE KIT</text>
    <text class="tagline" x="187" y="259" font-size="26">Genuine</text>
    <text class="tagline" x="190" y="286" font-size="26">parts</text>
    <g class="badges">
      <rect x="357" y="334" width="91" height="18" rx="3" class="red"/>
      <text class="badge-text" x="402" y="347" text-anchor="middle">DURABLE</text>
      <rect x="357" y="362" width="91" height="18" rx="3" fill="var(--brand-blue)"/>
      <text class="badge-text" x="402" y="375" text-anchor="middle" font-size="8.5">LONGLASTING</text>
      <rect x="357" y="390" width="91" height="18" rx="3" fill="var(--ink)"/>
      <text class="badge-text" x="402" y="403" text-anchor="middle" font-size="8.5">BESTQUALITY</text>
    </g>
    <g class="brand-mark">
      <circle cx="200" cy="425" r="44" fill="#a9a9a9"/>
      <text class="brand-name" x="200" y="502" text-anchor="middle">VARONEL</text>
    </g>
  </g>

  <!-- Bottom closure flap -->
  <g class="bottom-flap">
    <rect class="panel-face" x="98" y="529" width="370" height="86"/>
    <rect class="red" x="98" y="529" width="79" height="86"/>
    <path class="red" d="M98,615 H468 V625 Q468,680 413,680 H153 Q98,680 98,625 Z"/>
    <text class="headline" x="124" y="572" font-size="21">BRAKE SHOE KIT</text>
    <text class="headline-light" x="124" y="572" font-size="21" clip-path="url(#stripBottomFlap)">BRAKE SHOE KIT</text>
    <text class="tagline" x="183" y="595" font-size="18">Genuine parts</text>
    <ellipse class="product-thumb" cx="405" cy="572" rx="44" ry="36" role="img" aria-label="Small photo of the brake shoe pair"/>
  </g>

  <!-- Side panel B with dust flaps -->
  <g class="side-panel">
    <polygon class="red" points="470,159 490,83 548,83 560,159"/>
    <rect class="red" x="468" y="159" width="92" height="370"/>
    <polygon class="red" points="468,529 560,529 546,605 482,605"/>
    <g transform="translate(512,500) rotate(-90)">
      <text class="side-title" x="0" y="0" font-size="31">BRAKE SHOE KIT</text>
      <text class="side-sub" x="22" y="26" font-size="20">Genuine parts</text>
    </g>
  </g>

  <!-- Top closure flap -->
  <g class="top-flap">
    <path class="red" d="M560,73 V63 Q560,8 615,8 H875 Q930,8 930,63 V73 Z"/>
    <rect class="panel-face" x="560" y="73" width="370" height="86"/>
    <rect class="red" x="560" y="73" width="78" height="86"/>
    <text class="headline" x="585" y="116" font-size="21">BRAKE SHOE KIT</text>
    <text class="headline-light" x="585" y="116" font-size="21" clip-path="url(#stripTopFlap)">BRAKE SHOE KIT</text>
    <text class="tagline" x="645" y="139" font-size="18">Genuine parts</text>
    <ellipse class="product-thumb" cx="867" cy="113" rx="44" ry="36" role="img" aria-label="Small photo of the brake shoe pair"/>
  </g>

  <!-- Back panel -->
  <g class="back-panel">
    <rect class="panel-face" x="560" y="159" width="370" height="370"/>
    <rect class="red" x="560" y="159" width="78" height="370"/>
    <text class="strip-copy" transform="translate(582,510) rotate(-90)">Aluminum Alloy Motorcycle Brake Shoe With Spring</text>
    <rect class="product-photo" x="724" y="238" width="206" height="290" rx="90" role="img" aria-label="Photo of a motorcycle drum brake shoe pair with springs"/>
    <text class="headline" x="615" y="222" font-size="29">BRAKE SHOE KIT</text>
    <text class="headline-light" x="615" y="222" font-size="29" clip-path="url(#stripFront2)">BRAKE SHOE KIT</text>
    <text class="tagline" x="648" y="259" font-size="26">Genuine</text>
    <text class="tagline" x="651" y="287" font-size="26">parts</text>
    <g class="badges">
      <rect x="818" y="335" width="91" height="18" rx="3" class="red"/>
      <text class="badge-text" x="863" y="348" text-anchor="middle">DURABLE</text>
      <rect x="818" y="363" width="91" height="18" rx="3" fill="var(--brand-blue)"/>
      <text class="badge-text" x="863" y="376" text-anchor="middle" font-size="8.5">LONGLASTING</text>
      <rect x="818" y="391" width="91" height="18" rx="3" fill="var(--ink)"/>
      <text class="badge-text" x="863" y="404" text-anchor="middle" font-size="8.5">BESTQUALITY</text>
    </g>
    <g class="brand-mark">
      <circle cx="660" cy="425" r="44" fill="#a9a9a9"/>
      <text class="brand-name" x="660" y="502" text-anchor="middle">VARONEL</text>
    </g>
  </g>

  <!-- Glue flap -->
  <polygon class="red" points="930,162 974,175 978,522 930,529"/>
</svg>
</body>
</html>
```